Bramble Travel Planners needs an bold logo and business card design

Thanks you all for helping me with this project your assistance is appriciated
I am starting a home based travel agency and I need a bold and eye catching logo and business card designed.
I want to convey a sense of FREEDOM, expertise, customer service for travel customers
Bramble travel planners is a full service travel agency focused on customer service and adding value to a vacation and travel planning.
my idea is for a card that looks like an cruise ship boarding pass or passport with stamps with a back drop of beautiful beach scene, resort hotel and happiness.
The logo should be eye catching, unique but give a sense of freedom and it should be travel related
We want to give customers a sense of Freedom from travel planning, freedom from researching cruises and hotels and freedom to enjoy a wonderful cost effective vacation.

Target Market(s)

Customers considering travel for vacations, family reunions, business and weddings

Industry/Entity Type

Travel Industry

Contact Information for Business Card

Bramble Travel Planners
Warren Pelfrey Owner
WPelfrey@BrambleTravelPlanners.com
BrambleTravelPlanners.com
(555) 014-2287

Logo Text

“One’s destination is never a place, but a new way of seeing things.”

Font styles to use
Serif

Colors
85cae6
0492cd
ec1f27
e667a6
b768aa
33b8a4

Requirements
Must have
• The Logo you create should be on the busoness card
• should be clean, easy to read and attractive
• something you that would make you want to work with a travel agent
Nice to have
• should have cruise ship, hotel on the card or something that conveys travel
Should not have
• Should not have the american flag
• no yellow on the card

```html
<!DOCTYPE html>
<html lang="en">
<head>
<meta charset="utf-8">
<title>Bramble Travel Planners – Business Card</title>
<link rel="stylesheet" href="https://fonts.googleapis.com/css2?family=Libre+Baskerville:wght@400;700&display=swap">
<style>
  :root {
    --canvas: #ecebe8;
    --orchid: #b565a7;
    --paper: #ffffff;
    --paper-grey: #e9e8ea;
    --teal: #2aa58e;
    --sky: #85cae6;
    --ink-light: #ffffff;
  }
  * { box-sizing: border-box; margin: 0; padding: 0; }
  html, body {
    width: 1200px; height: 870px; overflow: hidden;
    background: var(--canvas);
    font-family: "Libre Baskerville", Georgia, serif;
  }
  .sheet {
    position: relative; width: 1200px; height: 870px;
    display: flex; justify-content: center; align-items: center; gap: 70px;
  }
  .card {
    width: 380px; height: 665px;
    box-shadow: 0 6px 18px rgba(0,0,0,.18);
    position: relative;
  }

  /* Front */
  .card-front {
    background: var(--orchid);
    padding: 16px;
    display: flex; flex-direction: column;
  }
  .front-logo-area {
    background: var(--paper);
    height: 330px;
    display: flex; flex-direction: column; align-items: center; justify-content: center;
    gap: 22px;
  }
  .brand-mark {
    width: 74px; height: 74px; border-radius: 50%;
    background: var(--sky);
  }
  .brand-name {
    color: var(--teal);
    font-weight: 700;
    font-size: 30px;
    line-height: 1.2;
    text-align: center;
    letter-spacing: .5px;
  }
  .front-details {
    flex: 1;
    margin-top: 10px;
    border: 3px solid var(--paper);
    display: flex; flex-direction: column;
    color: var(--ink-light);
    text-align: center;
  }
  .person {
    height: 120px;
    border-bottom: 3px solid var(--paper);
    display: flex; flex-direction: column; justify-content: center;
  }
  .person-name { font-size: 27px; font-weight: 700; }
  .person-role { font-size: 18px; margin-top: 2px; }
  .contact {
    flex: 1;
    display: flex; flex-direction: column; justify-content: center;
    gap: 12px;
    font-size: 14.5px;
  }

  /* Back */
  .card-back {
    background: var(--paper-grey);
    display: flex; flex-direction: column; align-items: center; justify-content: center;
    gap: 26px;
    padding-bottom: 120px;
  }
  .card-back .brand-mark { width: 90px; height: 90px; }
  .card-back .brand-name { font-size: 34px; }
</style>
</head>
<body>
<main class="sheet">
  <section class="card card-front" aria-label="Business card front">
    <div class="front-logo-area">
      <div class="brand-mark" aria-hidden="true"></div>
      <p class="brand-name">Bramble<br>Travel Planners</p>
    </div>
    <div class="front-details">
      <div class="person">
        <p class="person-name">Warren Pelfrey</p>
        <p class="person-role">Owner</p>
      </div>
      <div class="contact">
        <p class="contact-phone">(555) 014-2287</p>
        <p class="contact-web">BrambleTravelPlanners.com</p>
        <p class="contact-email">WPelfrey@BrambleTravelPlanners.com</p>
      </div>
    </div>
  </section>

  <section class="card card-back" aria-label="Business card back">
    <div class="brand-mark" aria-hidden="true"></div>
    <p class="brand-name">Bramble<br>Travel Planners</p>
  </section>
</main>
</body>
</html>
```